Business IT Services Billboard to attract local small businesses

We are Brivolane, a premier Managed Service Provider (MSP) specializing in comprehensive IT services and VOIP phone solutions exclusively for businesses. Our goal is to create a dynamic and visually engaging billboard advertisement that not only highlights our cutting-edge IT solutions but also emphasizes our state-of-the-art VOIP phone services. This billboard should communicate our commitment to providing innovative, reliable, and holistic technology solutions.
Target Market(s)
small business
Industry/Entity Type
Information Technology
Colors
Designer to choose colors to be used in the design.
Look and feel
Each slider illustrates characteristics of the customer's brand and the style your logo design should communicate.

```html
<!DOCTYPE html>
<html lang="en">
<head>
<meta charset="utf-8">
<title>Brivolane – Billboard</title>
<link href="https://fonts.googleapis.com/css2?family=Montserrat:wght@800&family=Nunito:ital,wght@0,400;0,900;1,700;1,800&display=swap" rel="stylesheet">
<style>
  :root {
    --brand-blue: #0d69ae;
    --brand-blue-deep: #0b5c9c;
    --violet: #6f6fc4;
    --violet-soft: #b9b8e3;
    --ink-grey: #4a4a4c;
    --white: #ffffff;
  }
  * { box-sizing: border-box; margin: 0; padding: 0; }
  html, body { width: 1200px; height: 753px; overflow: hidden; background: var(--white); }

  .billboard {
    position: relative;
    width: 1200px;
    height: 753px;
    overflow: hidden;
    background: var(--white);
    font-family: "Nunito", sans-serif;
  }

  .hero-photo {
    position: absolute;
    top: 0; right: 0; bottom: 0;
    left: 520px;
    background:
      radial-gradient(circle at 82% 48%, rgba(255,120,170,.45) 0 3%, transparent 12%),
      radial-gradient(ellipse at 78% 45%, #4a4f9e 0%, #6466b8 35%, transparent 70%),
      linear-gradient(160deg, #dcdcf2 0%, #9d9cd6 40%, #5c5fb0 70%, #3f4a98 100%);
    -webkit-mask-image: linear-gradient(90deg, transparent 0%, #000 32%);
            mask-image: linear-gradient(90deg, transparent 0%, #000 32%);
  }

  .brand-name {
    position: absolute;
    left: 72px;
    top: 78px;
    font-family: "Montserrat", sans-serif;
    font-weight: 800;
    font-size: 100px;
    line-height: 1;
    letter-spacing: -1px;
    color: var(--brand-blue);
  }

  .headline-band {
    position: absolute;
    left: 0; right: 0;
    top: 226px;
    height: 308px;
    background: linear-gradient(90deg,
      var(--brand-blue-deep) 0%,
      var(--brand-blue) 30%,
      rgba(60,110,190,.85) 55%,
      rgba(100,105,200,.35) 80%,
      rgba(100,105,200,0) 100%);
  }

  .headline {
    position: absolute;
    left: 70px;
    top: 250px;
    color: var(--white);
    font-size: 76px;
    line-height: 80px;
    font-weight: 900;
    letter-spacing: -0.5px;
    text-shadow: 0 3px 8px rgba(0,0,0,.25);
  }
  .headline .light { font-weight: 400; }

  .subhead {
    position: absolute;
    left: 72px;
    top: 562px;
    font-style: italic;
    font-weight: 800;
    font-size: 33px;
    line-height: 46px;
    color: var(--ink-grey);
  }

  .cta-band {
    position: absolute;
    right: 0; bottom: 0;
    width: 520px;
    height: 140px;
    background: linear-gradient(90deg, rgba(40,100,190,0) 0%, rgba(30,95,180,.75) 45%, #1e5fb4 100%);
  }

  .cta {
    position: absolute;
    right: 20px;
    top: 622px;
    text-align: right;
    color: var(--white);
  }
  .cta-lead {
    font-style: italic;
    font-weight: 700;
    font-size: 19px;
    line-height: 26px;
  }
  .cta-url {
    font-style: italic;
    font-weight: 800;
    font-size: 28px;
    line-height: 34px;
  }
</style>
</head>
<body>
  <main class="billboard">
    <div class="hero-photo" role="img" aria-label="Photo of a modern office VOIP desk phone with glowing network connection lines"></div>

    <div class="brand-name">Brivolane</div>

    <div class="headline-band"></div>
    <h1 class="headline">
      Seamless Technology<br>
      <span class="light">Solutions for</span> Modern<br>
      Businesses
    </h1>

    <p class="subhead">
      IT and VOIP Solutions<br>
      Tailored for Your<br>
      Business Success
    </p>

    <div class="cta-band"></div>
    <div class="cta">
      <p class="cta-lead">Transform Your Tech Today at</p>
      <p class="cta-url">www.brivolane.com</p>
    </div>
  </main>
</body>
</html>
```